Menu Re-Design for The Marlowbrook a british eatery in spanish holiday resort

Looking for a new design for our breakfast and lunch menu....

I have included some pictures of a few menus I like the feel of File No 1,2,3,4,5..... but am open to any ideas you may have....

The menu is to be double sided consisting of a front design with actual menu on reverse....

I have also included the relevant text files you will require...

We do not have a logo or set colour scheme to follow...

Target Market(s)

Predominantly British holidaymakers in popular Spanish resort....

Requirements
Must have
• Menu to be A3 and double sided, split between either a front page design and menu on reverse, or menu divided between both sides....
• Company Name:- The Marlowbrook
Nice to have
• Fun and Bold design whilst maintaining a feel of quality....
Should not have
• Please avoid the use of any food photography....

```html
<!DOCTYPE html>
<html lang="en">
<head>
<meta charset="utf-8">
<title>The Marlowbrook – Breakfast and Lunch Menu</title>
<link href="https://fonts.googleapis.com/css2?family=Josefin+Sans:wght@600;700&family=Rye&family=Yellowtail&display=swap" rel="stylesheet">
<style>
  :root{
    --backdrop:#262e33;
    --paper:#dcd8d2;
    --ink:#2a2a2a;
    --ink-soft:#4a4a4a;
    --red:#b3262a;
    --red-deep:#8e1b1f;
    --art-light:#c9c5bf;
    --art-dark:#8f8b86;
  }
  *{box-sizing:border-box;margin:0;padding:0}
  html,body{width:1200px;height:1200px;overflow:hidden;background:var(--backdrop)}
  body{position:relative;font-family:"Josefin Sans",sans-serif;color:var(--ink)}

  .sheet{position:absolute;left:50px;width:1100px;height:540px;background:var(--paper);box-shadow:0 18px 40px rgba(0,0,0,.45);overflow:hidden}
  .sheet--cover{top:40px}
  .sheet--menu{top:620px;padding:34px 40px;display:grid;grid-template-columns:1.15fr 1fr 1fr;gap:34px}

  /* cover */
  .cover-art{position:absolute;inset:0;background:
      radial-gradient(ellipse at 20% 30%,var(--art-dark) 0%,transparent 45%),
      radial-gradient(ellipse at 80% 70%,var(--art-dark) 0%,transparent 40%),
      radial-gradient(ellipse at 70% 15%,#a9a59f 0%,transparent 35%),
      linear-gradient(135deg,var(--art-light),#b3afa9)}
  .cover-title{position:absolute;left:50%;top:50%;transform:translate(-50%,-50%);text-align:center;
      background:var(--paper);padding:44px 64px;border:2px solid var(--red);white-space:nowrap}
  .cover-title__the{font-size:30px;letter-spacing:.35em;color:var(--red-deep);font-weight:700}
  .cover-title__name{font-size:78px;letter-spacing:.12em;color:var(--red-deep);font-weight:700;line-height:1.05;margin-top:8px}
  .cover-title__tag{font-size:20px;letter-spacing:.3em;color:var(--ink);font-weight:700;margin-top:18px}
  .cover-web{position:absolute;right:22px;bottom:18px;font-size:14px;letter-spacing:.25em;color:var(--red);font-weight:700}

  /* menu */
  .section-title{font-family:"Rye",serif;color:var(--red);font-size:40px;line-height:1;margin-bottom:12px}
  .section-title--stack{font-size:30px;line-height:1.05}
  .script{font-family:"Yellowtail",cursive;color:var(--red);font-size:34px;line-height:1.1;margin-bottom:10px}
  .intro{font-size:12px;font-weight:700;text-transform:uppercase;line-height:1.35;color:var(--ink-soft);margin-bottom:12px}
  .dish{margin-bottom:10px}
  .dish__name{font-size:17px;font-weight:700;color:var(--red);text-transform:uppercase}
  .dish__desc{font-size:12px;font-weight:700;text-transform:uppercase;line-height:1.35}
  .note{font-size:12px;font-weight:700;text-transform:uppercase;margin:6px 0 14px}
  .band{background:var(--red);color:var(--paper);font-size:16px;letter-spacing:.4em;font-weight:700;text-align:center;padding:8px 0 5px;margin-bottom:12px;white-space:nowrap}
  .price-list{list-style:none}
  .price-list li{display:flex;justify-content:space-between;gap:10px;font-size:13px;font-weight:700;text-transform:uppercase;padding:4px 0;border-bottom:1px dotted var(--ink-soft)}
  .col{min-width:0}
  .col--framed{border-left:1px solid var(--ink-soft);padding-left:28px}
  .small-head{font-size:12px;font-weight:700;color:var(--red);text-transform:uppercase;line-height:1.3;margin:16px 0 6px;letter-spacing:.05em}
</style>
</head>
<body>
  <section class="sheet sheet--cover">
    <div class="cover-art" role="img" aria-label="Hand-drawn ink and wash illustrations of burgers, onion rings, breakfast plates and drinks scattered across the cover"></div>
    <div class="cover-title">
      <div class="cover-title__the">THE</div>
      <div class="cover-title__name">MARLOWBROOK</div>
      <div class="cover-title__tag">BREAKFAST AND LUNCH</div>
    </div>
    <div class="cover-web">WWW.THEMARLOWBROOKEATERY.COM</div>
  </section>

  <section class="sheet sheet--menu">
    <div class="col">
      <h2 class="section-title">BREAKFAST</h2>
      <p class="intro">All our breakfast ingredients are of the highest quality available, sourced directly from the UK and freshly cooked to order</p>
      <div class="dish">
        <div class="dish__name">Marlowbrook</div>
        <div class="dish__desc">Bacon, fried egg, sausage, beans or grilled tomato, toast and butter</div>
      </div>
      <div class="dish">
        <div class="dish__name">Big Brook</div>
        <div class="dish__desc">2 bacon, 2 fried eggs, 2 sausage, beans or grilled tomato, toast and butter</div>
      </div>
      <p class="note">Free tea, coffee or orange juice</p>
      <div class="band">SOMETHING SPECIAL</div>
      <div class="dish">
        <div class="dish__name">Eggs Benedict</div>
        <div class="dish__desc">Traditional eggs benedict with baked ham on a toasted muffin with hollandaise</div>
      </div>
    </div>

    <div class="col col--framed">
      <h2 class="section-title section-title--stack">BUILD YOUR OWN BREAKFAST</h2>
      <ul class="price-list">
        <li><span>Sausage</span><span>1.00</span></li>
        <li><span>Fried egg</span><span>1.00</span></li>
        <li><span>Bacon</span><span>1.00</span></li>
        <li><span>Beans</span><span>0.80</span></li>
        <li><span>Black pudding</span><span>1.00</span></li>
        <li><span>Grilled tomato</span><span>0.80</span></li>
        <li><span>Hash brown</span><span>0.80</span></li>
        <li><span>Mushrooms</span><span>0.80</span></li>
        <li><span>Scrambled egg</span><span>1.20</span></li>
      </ul>
    </div>

    <div class="col col--framed">
      <div class="script">On the sides</div>
      <ul class="price-list">
        <li><span>Chips</span><span>2.00</span></li>
        <li><span>Cheesy chips</span><span>2.50</span></li>
        <li><span>Onion rings</span><span>2.00</span></li>
        <li><span>Garlic bread</span><span>2.50</span></li>
        <li><span>Cheesy chilli nachos</span><span>4.50</span></li>
      </ul>
      <div class="small-head">Chicken breast – add any extra of your choice</div>
      <ul class="price-list">
        <li><span>Onion</span><span>0.50</span></li>
        <li><span>Cheddar cheese</span><span>1.00</span></li>
        <li><span>Bacon</span><span>1.00</span></li>
        <li><span>Chilli con carne</span><span>2.00</span></li>
        <li><span>Spicy potato wedges</span><span>2.00</span></li>
      </ul>
    </div>
  </section>
</body>
</html>
```